Letterhead & Business Card Design Project

Use existing logo to create a new letterhead and business card design. Looking for something clean modern using color options of black, white and gray. The green from the logo may be used lightly as an accent color.

Target Market(s)

Professional business people

Industry/Entity Type

Business

Requirements
Must have
• Business card with front and back design using existing logo.
Nice to have
• Professional presentation
Clean look
Should not have
• No oil rigs, pumpjacks or clip art.

```html
<!DOCTYPE html>
<html lang="en">
<head>
<meta charset="utf-8">
<title>Kestrel Ridge Business Card</title>
<link href="https://fonts.googleapis.com/css2?family=Questrial&display=swap" rel="stylesheet">
<style>
  :root {
    --backdrop: #3b3b3b;
    --card-light: #f4f4f2;
    --card-dark: #0c0c0c;
    --ink: #1a1a1a;
    --ink-light: #e6e6e6;
    --accent: #22b022;
    --bar-gray: #7d7d7d;
  }
  * { margin: 0; padding: 0; box-sizing: border-box; }
  html, body {
    width: 1200px;
    height: 1000px;
    overflow: hidden;
    background: var(--backdrop);
    font-family: "Questrial", sans-serif;
  }
  .card {
    position: absolute;
    width: 530px;
    height: 303px;
  }
  .card--front { left: 180px; top: 168px; background: var(--card-light); color: var(--ink); }
  .card--back { left: 472px; top: 549px; background: var(--card-dark); color: var(--ink-light); }

  .accent-bar {
    position: absolute;
    left: 0;
    top: 64px;
    width: 13px;
    height: 87px;
    background: var(--accent);
  }
  .footer-bar {
    position: absolute;
    right: 0;
    bottom: 0;
    width: 265px;
    height: 12px;
    background: var(--bar-gray);
  }
  .wordmark {
    position: absolute;
    right: 32px;
    top: 76px;
    font-size: 27px;
    letter-spacing: 3px;
    line-height: 1;
    white-space: nowrap;
  }
  .card--front .wordmark { color: var(--ink); }
  .card--back .wordmark { color: var(--ink-light); top: 82px; }

  .website {
    position: absolute;
    left: 266px;
    bottom: 22px;
    font-size: 13px;
  }
  .card--back .website { left: 265px; }
  .website .domain { color: var(--accent); font-weight: bold; }

  .person {
    position: absolute;
    left: 40px;
    top: 68px;
  }
  .person__name { font-size: 17px; font-weight: bold; line-height: 20px; }
  .person__title { font-size: 13px; line-height: 18px; }

  .contact {
    position: absolute;
    left: 40px;
    top: 176px;
    font-size: 12.5px;
    line-height: 15px;
  }
  .contact__label { color: var(--accent); }
  .address {
    position: absolute;
    left: 40px;
    top: 237px;
    font-size: 12.5px;
    line-height: 15px;
  }
</style>
</head>
<body>
  <section class="card card--front" aria-label="Business card front">
    <div class="accent-bar"></div>
    <div class="person">
      <p class="person__name">Daniel R Hayes</p>
      <p class="person__title">Managing Member</p>
    </div>
    <div class="wordmark">KESTREL RIDGE</div>
    <div class="contact">
      <p><span class="contact__label">Phone:</span> 555.214.0193</p>
      <p><span class="contact__label">Cell:</span> 555.307.6642</p>
      <p><span class="contact__label">Fax:</span> 555.214.0194</p>
    </div>
    <div class="address">
      <p>4120 North Alder St</p>
      <p>Suite 210, Fairview</p>
      <p>Ohio 43210</p>
    </div>
    <p class="website">www.<span class="domain">kestrelridge</span>.com</p>
    <div class="footer-bar"></div>
  </section>

  <section class="card card--back" aria-label="Business card back">
    <div class="accent-bar"></div>
    <div class="wordmark">KESTREL RIDGE</div>
    <p class="website">www.<span class="domain">kestrelridge</span>.com</p>
    <div class="footer-bar"></div>
  </section>
</body>
</html>
```